I need cover art for my first album

I am releasing my first album and I need cover art for the CD  packaging. The art would also be used in Tunevale and other streaming services. The music is dark, experimental electronic music. It includes lots of soundscapes with industrial, metallic sounds. Similar artists include Grevhald and Ivor Pennick. The album's concept is inspired by the loneliness and inherent dangers of long-term space travel and living alone in cold, distant space stations.
You can hear a rough cut of one of the tracks for the album at https://echoloft.net/kelvorant/tidegrove.

Colors
Designer to choose colors to be used in the design.
Requirements
Must have
- The design should be abstract and minimalist but not only grayscale. I would like to see color used in ways that convey feelings. Provide a sense of movement.
Should not have
- No images of moons or planets. Please don't be literal with the "space" theme.

```html
<!DOCTYPE html>
<html lang="en">
<head>
<meta charset="utf-8">
<title>Silent Beyond Tideline — Album Cover</title>
<link rel="stylesheet" href="https://fonts.googleapis.com/css2?family=Raleway:wght@400&display=swap">
<style>
  :root {
    --navy-deep: #0f2133;
    --navy-light: #21435a;
    --cream: #fde6d3;
    --teal-light: #6fd0c4;
    --teal-deep: #0b6b58;
    --coral: #d97656;
    --sand: #e9dc9b;
    --oxblood: #730a0a;
    --title: #d9dde1;
  }
  html, body {
    margin: 0;
    padding: 0;
    width: 1200px;
    height: 1200px;
    overflow: hidden;
    background: var(--navy-deep);
  }
  .cover {
    position: relative;
    width: 1200px;
    height: 1200px;
    overflow: hidden;
    background: radial-gradient(circle at 90% 10%, var(--navy-light) 0%, #173247 45%, var(--navy-deep) 100%);
  }
  .cover__artwork {
    position: absolute;
    inset: 0;
    width: 1200px;
    height: 1200px;
  }
  .cover__title {
    position: absolute;
    right: 38px;
    top: 1068px;
    margin: 0;
    font-family: "Raleway", sans-serif;
    font-weight: 400;
    font-size: 45px;
    letter-spacing: 3.5px;
    line-height: 1;
    color: var(--title);
    text-transform: uppercase;
    white-space: nowrap;
  }
</style>
</head>
<body>
  <main class="cover">
    <svg class="cover__artwork" viewBox="0 0 1200 1200" xmlns="http://www.w3.org/2000/svg">
      <defs>
        <linearGradient id="ribbon-tones" x1="0" y1="1" x2="1" y2="0">
          <stop offset="0%" stop-color="var(--teal-deep)" />
          <stop offset="25%" stop-color="var(--coral)" />
          <stop offset="45%" stop-color="var(--cream)" />
          <stop offset="60%" stop-color="var(--teal-light)" />
          <stop offset="75%" stop-color="var(--sand)" />
          <stop offset="100%" stop-color="var(--coral)" />
        </linearGradient>
      </defs>
      <path class="cover__ribbons" role="img"
            aria-label="Tangled hand-drawn ribbons in cream, teal, coral, sand and oxblood sweeping diagonally from lower left to upper right"
            fill="url(#ribbon-tones)" opacity="0.85"
            d="M0 790 C140 700 300 560 420 420 C480 300 520 160 580 110 C700 40 820 20 900 0 L1200 0 L1200 660 C1120 720 1060 800 1000 850 C920 880 860 780 800 760 C700 800 600 900 520 950 C420 1000 340 1060 260 1090 L0 1100 Z" />
    </svg>
    <h1 class="cover__title">Silent Beyond Tideline</h1>
  </main>
</body>
</html>
```